Torvane Center for Restorative Medicine

I need a full informational website for my medical practice. I would like to use my logo and also include a lot of emblems/pictures (also a picture of me in a white coat). The website should have a function for people to inquire and send me messages. I will be offering needle-less regenerative injection therapy, stem cell treatments, bioidentical hormone therapy, treatment for chronic illness, neurodegenerative diseases, skin rejuvenation, hair restoration, male enhancement, female enhancement, and anti-aging. The practice will not be accepting insurance and will be cash/credit card only.
A good example of written content and functionality is this website:
http://thebqvx.example/. However, I want different theme and tones.
Target Market(s)
High end clientele in Los Angeles, Southern California. Health minded people who are interested in living better and longer and can afford anti-aging treatments. Men and women who want to improve sexual health and wellbeing.
Industry/Entity Type
Medical And Science
Coding
Coded - Design and coding required
Number of Pages Required
5+ page
Font styles to use
Requirements
Must have
- 1. I will need to be able to move the site to other servers (needed for site speed)
- 2. Site must be build on WordPress
- 3. Full admin credentials for domain, cpanel, wordpress, ftp.
- 4. No third party interaction on development and content deployment once the site is on different servers
- 5. I will need the ability to add content and links to the site
- 6. I will need the ability to optimize the site for speed
- 7. I will need to ability to modify URLs so they are more SEO friendly
Nice to have
- pictures of stem cells, health improvement and regeneration, beauty, youthful individuals, older healthy and happy individuals. Medical designs.
Should not have
- flowers, dna

```html
<!DOCTYPE html>
<html lang="en">
<head>
<meta charset="utf-8">
<title>Torvane Center for Restorative Medicine</title>
<link href="https://fonts.googleapis.com/css2?family=Montserrat:wght@400;500;600;700&display=swap" rel="stylesheet">
<style>
:root{
  --teal:#7ecfc1;
  --teal-deep:#5fbba9;
  --teal-text:#5cb8a8;
  --blue:#86c9ea;
  --ink:#1d1f24;
  --body:#6b6f76;
  --light:#f6f7f7;
  --hero:#e8f3f4;
  --footer:#1b1e26;
  --white:#ffffff;
}
*{box-sizing:border-box;margin:0;padding:0}
html,body{width:1200px;height:3593px;overflow:hidden}
body{font-family:"Montserrat",sans-serif;color:var(--ink);background:var(--white);position:relative}
section,header,footer{position:absolute;left:0;width:1200px}
.abs{position:absolute}
.fill{display:block}

/* hero */
.hero{top:0;height:575px;background:linear-gradient(120deg,#f4fafb 0%,var(--hero) 55%,#dcedf0 100%);overflow:hidden}
.brand{left:96px;top:40px;display:flex;align-items:center;gap:12px}
.brand-dot{width:30px;height:30px;border-radius:50%;background:var(--teal-deep)}
.brand-name{font-size:26px;font-weight:700;color:#1f3e6b;letter-spacing:1px}
.nav{left:462px;top:50px;display:flex;gap:0;font-size:14px;color:#444}
.nav a{color:inherit;text-decoration:none;position:absolute;white-space:nowrap}
.call{left:1008px;top:40px;font-size:13px;font-weight:700}
.call span{display:block;color:var(--teal-text);font-weight:600;margin-top:3px}
.doctor{left:108px;top:120px;width:290px;height:455px;background:linear-gradient(180deg,#e9eef1,#ffffff 60%,#dfe8ec);border-radius:120px 120px 0 0}
.vials{left:410px;top:215px;width:380px;height:270px;background:radial-gradient(ellipse at center,#d4e2ea 0%,rgba(220,234,238,0) 70%)}
.appt{left:810px;top:148px;width:276px;height:360px;background:var(--white);box-shadow:0 6px 24px rgba(0,0,0,.08);padding:34px 24px 0;text-align:center}
.appt h2{font-size:19px;font-weight:700}
.appt p{font-size:12px;color:#555;margin:8px 0 24px}
.field{height:42px;border:1px solid #cfe8e3;font-size:12px;color:#666;text-align:left;padding:13px 10px;margin-bottom:12px}
.submit{height:40px;background:var(--teal);color:var(--white);font-size:12px;font-weight:700;line-height:40px;margin-top:18px}
.dots{left:538px;top:527px;display:flex;gap:12px;align-items:center}
.dots i{display:block;width:6px;height:5px;background:#b9c9cb;border-radius:2px}
.dots i.on{width:22px;background:var(--teal)}

/* about */
.about{top:575px;height:450px;background:var(--light)}
.eyebrow{font-size:17px;font-weight:600}
.about .eyebrow{left:96px;top:93px}
.about h2{left:96px;top:120px;font-size:32px;font-weight:700}
.lede{font-size:12.5px;line-height:20px;color:var(--body)}
.about .lede{left:96px;top:190px;width:670px}
.more{font-size:12px;font-weight:600;color:var(--teal-text);border-left:3px solid var(--teal);padding:14px 0 14px 18px}
.about .more{left:96px;top:305px}
.about-main{left:797px;top:96px;width:310px;height:242px;background:linear-gradient(135deg,#d9c6b8,#8d7468 60%,#5b4a44)}
.about-small{left:750px;top:239px;width:148px;height:115px;background:linear-gradient(135deg,#eadbd0,#b99c8c);border:4px solid var(--light)}

/* services */
.services{top:1025px;height:450px;background:#fbfbfb}
.services-panel{left:0;top:0;width:414px;height:450px;background:var(--blue);color:var(--white);overflow:hidden}
.services-panel .eyebrow{left:93px;top:93px}
.services-panel h2{left:93px;top:116px;font-size:32px;font-weight:700}
.services-panel .lede{left:93px;top:176px;width:290px;color:#eef8fd;font-size:12px;line-height:19px}
.services-panel .more{left:93px;top:310px;color:var(--white);border-color:var(--white)}
.svc{width:220px;text-align:center;font-size:12px;font-weight:700;line-height:17px}
.svc svg{display:block;margin:0 auto 14px}

/* news */
.news{top:1475px;height:736px;background:var(--light)}
.news h2{left:0;width:1200px;text-align:center;top:90px;font-size:34px;font-weight:700}
.card{top:161px;width:318px;height:479px;background:var(--white);box-shadow:0 2px 10px rgba(0,0,0,.05)}
.card .photo{width:318px;height:239px}
.card .date{position:absolute;left:30px;top:272px;font-size:11px;color:var(--teal-text);font-weight:600}
.card h3{position:absolute;left:30px;top:290px;font-size:19px;font-weight:700}
.card .lede{position:absolute;left:30px;top:328px;width:262px;font-size:12px;line-height:19px}
.card .more{position:absolute;left:30px;top:405px}
.arrow{top:263px;width:32px;height:118px;display:flex;align-items:center;justify-content:center}

/* stats */
.stats{top:2211px;height:464px;background:var(--teal-deep);color:var(--white);overflow:hidden}
.stats-bg{left:680px;top:0;width:520px;height:464px;background:linear-gradient(90deg,rgba(255,255,255,0),rgba(255,255,255,.08))}
.stats h2{left:0;width:1200px;text-align:center;top:90px;font-size:32px;font-weight:700}
.stats .lede{left:200px;width:800px;top:138px;text-align:center;color:#e6f6f2;font-size:12px;line-height:19px}
.stat{top:238px;width:250px;text-align:center}
.stat b{display:block;font-size:26px;font-weight:700;margin-top:10px}
.stat span{font-size:13px}
.divider{top:222px;width:1px;height:150px;background:rgba(255,255,255,.35)}

/* map */
.map{top:2675px;height:482px;background:linear-gradient(135deg,#eef0ee,#e4e7e3)}
.contact{left:96px;top:98px;width:240px;height:288px;background:rgba(108,196,180,.92);color:var(--white);padding:28px 22px;font-size:12px}
.contact h3{font-size:16px;font-weight:500;margin-bottom:14px}
.contact .row{display:flex;align-items:center;gap:12px;margin-bottom:11px}
.contact .hours{display:flex;justify-content:space-between;margin-bottom:10px}

/* footer */
.footer{top:3157px;height:436px;background:var(--footer);color:var(--white)}
.footer h4{top:96px;font-size:15px;font-weight:700}
.links{top:150px;font-size:11.5px;color:#cfd2d8;line-height:31px;list-style:none}
.input{left:647px;width:459px;border:1px solid #3c414c;font-size:11px;color:#c8ccd3;padding:10px 10px}
.send{left:1003px;top:306px;width:103px;height:32px;background:var(--teal);color:var(--ink);font-size:12px;font-weight:700;text-align:center;line-height:32px}
.copy{left:0;width:1200px;top:393px;text-align:center;font-size:11px;color:#9ba0a9}
.copy span{color:var(--teal)}
</style>
</head>
<body>

<header class="hero">
  <div class="abs doctor fill" role="img" aria-label="Doctor in a white coat with arms crossed"></div>
  <div class="abs vials fill" role="img" aria-label="Syringe and medicine vial"></div>
  <div class="abs brand"><span class="brand-dot"></span><span class="brand-name">TORVANE</span></div>
  <nav class="abs nav">
    <a style="left:0;top:0">Home</a>
    <a style="left:94px;top:0">About</a>
    <a style="left:189px;top:0">Services</a>
    <a style="left:297px;top:0">Testimonials</a>
    <a style="left:431px;top:0">Contact</a>
  </nav>
  <div class="abs call">Call Us<span>01-555-010-247</span></div>
  <form class="abs appt">
    <h2>Request An Appoinment</h2>
    <p>Please Compleate the Form Below</p>
    <div class="field">Name</div>
    <div class="field">Email</div>
    <div class="field">Phone</div>
    <div class="submit">SUBMIT</div>
  </form>
  <div class="abs dots"><i class="on"></i><i></i><i></i></div>
</header>

<section class="about">
  <div class="abs eyebrow">About</div>
  <h2 class="abs">Torvane Center for Restorative Medicine</h2>
  <p class="abs lede">Lorem ipsum dolor sit amet, consectetur adipiscing elit. Pellentesque molestie sit amet ex eu interdum. Sed lectus leo, tempus vitae bibendum nec, pharetra ac justo. Donec posuere convallis feugiat. Praesent sed nunc dictum dolor fringilla placerat eget et ex. Sed orci nibh, vehicula a viverra id, pretium at lacus. Pellentesque imperdiet bibendum sem. Aenean gravida pharetra mauris id tempor. Sed id laoreet orci.</p>
  <div class="abs more">Read More</div>
  <div class="abs about-main fill" role="img" aria-label="Patient receiving a skin treatment"></div>
  <div class="abs about-small fill" role="img" aria-label="Smiling patient after treatment"></div>
</section>

<section class="services">
  <div class="abs services-panel">
    <div class="abs eyebrow">Our Special</div>
    <h2 class="abs">Services</h2>
    <p class="abs lede">Lorem ipsum dolor amet, consectetur adipiscing elit. Pellentesque molestie sit amet ex interdum. Sed lectus leo, tempus vitae bibendum nec, pharetra justo. Donec posuere convallis feugiat. Praesent sed nunc dictum dolor fringilla.</p>
    <div class="abs more">Read More</div>
  </div>
  <div class="abs svc" style="left:441px;top:100px">
    <svg width="60" height="56" viewBox="0 0 60 56" fill="none" stroke="#6cc3b3" stroke-width="2"><path d="M12 8l36 36M44 40l6 6M20 16l-6 6M26 22l24 24"/><rect x="22" y="20" width="28" height="9" transform="rotate(45 36 24)"/></svg>
    Needle-less Regenerative<br>Injection Therapy</div>
  <div class="abs svc" style="left:676px;top:100px">
    <svg width="60" height="56" viewBox="0 0 60 56" fill="none" stroke="#6cc3b3" stroke-width="2"><circle cx="30" cy="28" r="18"/><circle cx="30" cy="28" r="7"/><path d="M30 4v6M30 46v6M6 28h6M48 28h6"/></svg>
    Stem Cell Treatments</div>
  <div class="abs svc" style="left:915px;top:100px">
    <svg width="60" height="56" viewBox="0 0 60 56" fill="none" stroke="#6cc3b3" stroke-width="2"><path d="M24 6h12M26 6v16L12 48h36L34 22V6"/><path d="M17 38h26"/></svg>
    Bioidentical Hormone<br>Therapy</div>
  <div class="abs svc" style="left:441px;top:258px">
    <svg width="60" height="56" viewBox="0 0 60 56" fill="none" stroke="#6cc3b3" stroke-width="2"><rect x="10" y="26" width="40" height="22"/><path d="M20 26v-6h20v6M30 31v12M24 37h12"/></svg>
    Treatment For<br>Chronic Illness</div>
  <div class="abs svc" style="left:676px;top:258px">
    <svg width="60" height="56" viewBox="0 0 60 56" fill="none" stroke="#6cc3b3" stroke-width="2"><circle cx="30" cy="28" r="16"/><path d="M30 12v32M22 20c4 4 4 12 0 16M38 20c-4 4-4 12 0 16"/></svg>
    Neurodegenerative<br>Diseases</div>
  <div class="abs svc" style="left:915px;top:258px">
    <svg width="60" height="56" viewBox="0 0 60 56" fill="none" stroke="#6cc3b3" stroke-width="2"><circle cx="30" cy="26" r="13"/><path d="M14 52c2-9 8-13 16-13s14 4 16 13"/></svg>
    Skin Rejuvenation</div>
</section>

<section class="news">
  <h2 class="abs">Medical News</h2>
  <article class="abs card" style="left:96px">
    <div class="photo fill" role="img" aria-label="Vaccine injection in an arm" style="background:linear-gradient(135deg,#d07a98,#c9a89a 60%,#e8ddd5)"></div>
    <div class="date">Oct 04, 2018</div>
    <h3>Lorem ipsum dolor</h3>
    <p class="lede">Lorem ipsum dolor sit amet, consectetur adipiscing elit. Pellentesque molestie sit amet ex eu interdum. Sed lectus leo</p>
    <div class="more">Read More</div>
  </article>
  <article class="abs card" style="left:441px">
    <div class="photo fill" role="img" aria-label="Doctor examining a patient's back" style="background:linear-gradient(135deg,#f1ebe6,#cfae98 55%,#8b6f60)"></div>
    <div class="date">Oct 04, 2018</div>
    <h3>Lorem ipsum dolor</h3>
    <p class="lede">Lorem ipsum dolor sit amet, consectetur adipiscing elit. Pellentesque molestie sit amet ex eu interdum. Sed lectus leo</p>
    <div class="more">Read More</div>
  </article>
  <article class="abs card" style="left:788px">
    <div class="photo fill" role="img" aria-label="Hospital ward with beds" style="background:linear-gradient(135deg,#c9d3da,#eef1f3 50%,#9aa8b2)"></div>
    <div class="date">Oct 04, 2018</div>
    <h3>Lorem ipsum dolor</h3>
    <p class="lede">Lorem ipsum dolor sit amet, consectetur adipiscing elit. Pellentesque molestie sit amet ex eu interdum. Sed lectus leo</p>
    <div class="more">Read More</div>
  </article>
  <div class="abs arrow" style="left:96px;background:rgba(40,40,40,.55)"><svg width="12" height="30" viewBox="0 0 12 30"><path d="M10 2L2 15l8 13" fill="none" stroke="#fff" stroke-width="2"/></svg></div>
  <div class="abs arrow" style="left:1074px;background:rgba(126,207,193,.9)"><svg width="12" height="30" viewBox="0 0 12 30"><path d="M2 2l8 13-8 13" fill="none" stroke="#fff" stroke-width="2"/></svg></div>
</section>

<section class="stats">
  <div class="abs stats-bg fill" role="img" aria-label="Stethoscope and laptop on a desk"></div>
  <h2 class="abs">Important Static</h2>
  <p class="abs lede">Lorem ipsum dolor amet, consectetur adipiscing elit. Pellentesque molestie sit amet ex eu interdum. Sed lectus leo, tempus vitae bibendum nec, pharetra justo. Donec posuere convallis feugiat. Praesent sed nunc dictum dolor fringilla</p>
  <div class="abs stat" style="left:86px">
    <svg width="62" height="50" viewBox="0 0 62 50" fill="#fff"><circle cx="31" cy="12" r="9"/><circle cx="13" cy="17" r="6"/><circle cx="49" cy="17" r="6"/><path d="M16 48c0-12 6-20 15-20s15 8 15 20z"/><path d="M2 46c0-10 4-16 11-16 3 0 5 1 6 2-3 4-4 9-4 14zM60 46c0-10-4-16-11-16-3 0-5 1-6 2 3 4 4 9 4 14z"/></svg>
    <b>2000k</b><span>Lorem ipsum</span></div>
  <div class="abs divider" style="left:343px"></div>
  <div class="abs stat" style="left:337px">
    <svg width="62" height="50" viewBox="0 0 62 50" fill="none" stroke="#fff" stroke-width="3"><path d="M20 4v14a9 9 0 0018 0V4M29 27v8a10 10 0 0020 0v-6"/><circle cx="49" cy="24" r="5"/></svg>
    <b>320</b><span>Lorem ipsum</span></div>
  <div class="abs divider" style="left:602px"></div>
  <div class="abs stat" style="left:591px">
    <svg width="62" height="50" viewBox="0 0 62 50" fill="#fff"><rect x="4" y="8" width="5" height="38"/><rect x="4" y="30" width="54" height="8"/><rect x="53" y="24" width="5" height="22"/><circle cx="17" cy="23" r="5"/><rect x="25" y="20" width="28" height="8" rx="2"/></svg>
    <b>1000</b><span>Lorem ipsum</span></div>
  <div class="abs divider" style="left:860px"></div>
  <div class="abs stat" style="left:859px">
    <svg width="62" height="50" viewBox="0 0 62 50" fill="#fff"><path d="M22 4h18v8h-4V8H26v4h-4z"/><rect x="6" y="12" width="50" height="34" rx="5"/><path d="M27 19h8v7h7v8h-7v7h-8v-7h-7v-8h7z" fill="#5fbba9"/></svg>
    <b>52</b><span>Lorem ipsum</span></div>
</section>

<section class="map" role="img" aria-label="Street map of the clinic's area">
  <div class="abs contact">
    <h3>Contact Details</h3>
    <div class="row"><svg width="14" height="16" viewBox="0 0 14 16" fill="none" stroke="#fff" stroke-width="1.5"><path d="M7 15s5-5 5-9A5 5 0 002 6c0 4 5 9 5 9z"/><circle cx="7" cy="6" r="2"/></svg>45 BC making it over 2000</div>
    <div class="row"><svg width="14" height="16" viewBox="0 0 14 16" fill="none" stroke="#fff" stroke-width="1.5"><path d="M3 2l3 1 1 3-2 1c1 2 2 3 4 4l1-2 3 1 1 3-2 2C7 14 1 8 1 4z"/></svg>01-555-010-247</div>
    <div class="row"><svg width="14" height="16" viewBox="0 0 14 16" fill="none" stroke="#fff" stroke-width="1.5"><rect x="1" y="3" width="12" height="10"/><path d="M1 3l6 5 6-5"/></svg>info@torvane.example</div>
    <h3 style="margin-top:22px">Opening Hour</h3>
    <div class="hours"><span>Monday - Friday</span><span>10:00 to 5:00</span></div>
    <div class="hours"><span>Saturday</span><span>10:00 to 3:30</span></div>
  </div>
</section>

<footer class="footer">
  <h4 class="abs" style="left:93px">Quick Links</h4>
  <ul class="abs links" style="left:93px"><li>Home</li><li>About</li><li>Services</li><li>Testimonials</li><li>Contact</li></ul>
  <h4 class="abs" style="left:347px">Medical News</h4>
  <ul class="abs links" style="left:347px"><li>Lorem ipsum dolor</li><li>Donec lorem ante</li><li>Vestibulum consectetur</li><li>Nullam nisl erat</li></ul>
  <h4 class="abs" style="left:647px">Get In Touch</h4>
  <div class="abs input" style="top:146px;height:33px">Name</div>
  <div class="abs input" style="top:186px;height:33px">Email</div>
  <div class="abs input" style="top:225px;height:67px">Message</div>
  <div class="abs send">SEND</div>
  <div class="abs copy">© 2018 <span>Torvane Center for Restorative Medicine</span>. All Right Reserved.</div>
</footer>

</body>
</html>
```